Solar Energy Technology Company - Solar Savings Analysis Flyer

I Have Included The Text Content I Want Put On An 8 1/2 " x 11" Flyer.

I Want To See It In One Page Format And In Tri-Fold Brochure Format.

It Needs To Grab And Captivate Prospective Customers, Awesome Graphics, Layout, Etc.

We Are A Cutting Edge Solar Energy Solutions & Technology Company.

We Need A World Class High Tech Look and Logo For Our Company Included On Our 8 1/2 x 11 Flyer & Trifold Brochure

Brightfold Venture Partners, LLC
"Forward Ideas Delivered"

Would Like A Black Gold And Electric Blue Color Scheme, However, We We Are Open To Seeing Your Creativity, Colors, Graphics Etc. For Consideration.

Target Market(s)

Homeowners Without Solar Panels On Their Roof

Industry/Entity Type

New Roof Top Solar Energy Producing Panel Technology Systems

Font styles to use
Serif

Requirements
Must have
• See My Attached Flyer/Trifold Brochure Display Content
Nice to have
• Gold Black And Electric Blue Color Scheme, Solar Theme Background Graphics

```html
<!DOCTYPE html>
<html lang="en">
<head>
<meta charset="utf-8">
<title>Brightwave Solar – Savings Analysis Flyer</title>
<link href="https://fonts.googleapis.com/css2?family=Archivo+Black&family=Arimo:wght@400;700&family=Roboto+Condensed:wght@400;500;700&display=swap" rel="stylesheet">
<style>
  :root{
    --brand-blue:#27348b;
    --headline-blue:#1d3f88;
    --link-blue:#2a3a8c;
    --gold:#f0921c;
    --gold-deep:#e8702a;
    --panel-black:#1e1e1e;
    --ink:#1a1a1a;
    --paper:#ffffff;
    --page-bg:#e9e7e4;
  }
  *{margin:0;padding:0;box-sizing:border-box}
  html,body{width:1200px;height:1200px;overflow:hidden;background:var(--page-bg)}
  .flyer{position:absolute;left:174px;top:50px;width:851px;height:1100px;background:var(--paper);overflow:hidden;box-shadow:0 6px 18px rgba(0,0,0,.25)}
  .flyer-shapes,.hero-photo{position:absolute;left:0;top:0}
  .txt{position:absolute;line-height:1;white-space:nowrap}
  .cond{font-family:"Roboto Condensed",sans-serif}
  .sans{font-family:"Arimo",sans-serif}

  .brand{left:24px;top:60px;display:flex;align-items:center;gap:10px;font-family:"Roboto Condensed",sans-serif;font-weight:700;font-size:40px;color:var(--paper);letter-spacing:.2px}
  .brand-mark{width:22px;height:22px;background:var(--gold)}

  .attention{left:24px;top:203px;font-family:"Roboto Condensed",sans-serif;font-weight:500;font-size:66px;line-height:66px;color:var(--gold)}
  .question{left:24px;font-family:"Arimo",sans-serif;font-weight:700;font-size:27px;color:var(--paper)}
  .q1{top:352px}.q2{top:404px}.q3{top:456px}
  .amount{left:24px;top:518px;font-family:"Arimo",sans-serif;font-weight:700;font-size:60px;color:var(--gold)}
  .allow{left:382px;top:567px;font-family:"Arimo",sans-serif;font-weight:700;font-size:30px;color:var(--paper)}

  .centered{left:0;width:851px;text-align:center}
  .headline{font-family:"Archivo Black",sans-serif;font-size:41px;color:var(--headline-blue);letter-spacing:2px}
  .h1{top:630px}.h2{top:681px}
  .range{top:727px;font-family:"Roboto Condensed",sans-serif;font-weight:500;font-size:33px;color:var(--ink)}
  .pitch{top:771px;font-family:"Roboto Condensed",sans-serif;font-weight:500;font-size:18px;line-height:23.5px;color:var(--ink);white-space:normal}
  .visit{top:857px;font-family:"Roboto Condensed",sans-serif;font-weight:500;font-size:21px;line-height:27px;color:var(--ink);white-space:normal}
  .visit .web{font-family:"Arimo",sans-serif;font-weight:700;color:var(--link-blue)}
  .company{top:926px;font-family:"Arimo",sans-serif;font-weight:700;font-size:35px;color:var(--link-blue)}
  .phone{top:968px;font-family:"Arimo",sans-serif;font-weight:700;font-size:35px;color:var(--ink)}
  .tagline{top:1021px;font-family:"Arimo",sans-serif;font-weight:700;font-size:27px;color:var(--paper)}
  .offices{top:1070px;font-family:"Roboto Condensed",sans-serif;font-size:18px;color:#2a2a2a;display:flex;justify-content:center;gap:24px}
</style>
</head>
<body>
<main class="flyer">
  <svg class="flyer-shapes" width="851" height="1100" viewBox="0 0 851 1100" aria-hidden="true">
    <defs>
      <linearGradient id="goldStripe" x1="0" x2="1">
        <stop offset="0" stop-color="#e8702a"/><stop offset="1" stop-color="#f0921c"/>
      </linearGradient>
      <linearGradient id="darkWedge" x1="0" y1="0" x2="1" y2="1">
        <stop offset="0" stop-color="#3a3a48"/><stop offset="1" stop-color="#1e1e2a"/>
      </linearGradient>
      <linearGradient id="footerBand" x1="0" x2="1">
        <stop offset="0" stop-color="#f09a1a"/><stop offset="1" stop-color="#e8702a"/>
      </linearGradient>
    </defs>
    <rect x="0" y="0" width="851" height="148" fill="var(--brand-blue)"/>
    <rect x="0" y="148" width="851" height="436" fill="var(--panel-black)"/>
    <polygon points="0,148 478,148 458,180 0,180" fill="url(#goldStripe)"/>
    <polygon points="556,14 851,14 851,560 540,560 392,310" fill="url(#darkWedge)"/>
    <rect x="0" y="584" width="851" height="427" fill="var(--paper)"/>
    <polygon points="333,559 851,559 851,601 368,601" fill="var(--brand-blue)"/>
    <rect x="0" y="1011" width="851" height="47" fill="var(--brand-blue)"/>
    <rect x="0" y="1058" width="851" height="42" fill="url(#footerBand)"/>
  </svg>

  <svg class="hero-photo" width="851" height="600" viewBox="0 0 851 600" role="img" aria-label="Photo of rooftop solar panels in front of a hazy city skyline">
    <defs>
      <linearGradient id="photoTones" x1="0" y1="0" x2="1" y2="1">
        <stop offset="0" stop-color="#c9d6e2"/>
        <stop offset=".45" stop-color="#8fa3b8"/>
        <stop offset=".7" stop-color="#2f5fc4"/>
        <stop offset="1" stop-color="#1d3f9a"/>
      </linearGradient>
    </defs>
    <polygon points="590,37 851,37 851,559 551,559 398,310" fill="url(#photoTones)"/>
  </svg>

  <div class="txt brand"><span>BRIGHTWAVE SOLAR</span><span class="brand-mark"></span></div>

  <div class="txt attention">ATTENTION<br>HOMEOWNER!</div>
  <div class="txt question q1">Are You FED UP With</div>
  <div class="txt question q2">Your HIGH Electric Bills?</div>
  <div class="txt question q3">We Will Pay You</div>
  <div class="txt amount">$2,000…</div>
  <div class="txt allow">…When You Allow Us To</div>

  <div class="txt centered headline h1">PERMANENTLY LOWER YOUR</div>
  <div class="txt centered headline h2">ELECTRIC BILL</div>
  <div class="txt centered range">By At Least 25% To 50%!</div>
  <p class="txt centered pitch">On Average, We SAVE Homeowners *33% OFF Their Electricity Cost Every Month With Our NEW<br>Cutting Edge ADVANCED SOLAR TECHNOLOGY, WITHOUT TAKING 1 PENNY FROM YOUR CURRENT<br>MONTHLY BUDGET. GOVERNMENT SUBSIDIZED!</p>
  <p class="txt centered visit">Visit Our Website @ <span class="web">www.BrightwaveSolar.energy</span> To Request Your<br>Complimentary Energy Savings Analysis And To Accept Our $200 Gift.</p>
  <div class="txt centered company">Brightfold Venture Partners, LLC</div>
  <div class="txt centered phone">888-555-0142 Ext. 204 Dana Whitlow</div>
  <div class="txt centered tagline">“Forward Ideas Delivered”</div>
  <div class="txt centered offices"><span>Corp Office: 1520 W. Canyon Ave. Las Vegas, NV 89102</span><span>|</span><span>Regional Office: 885 Orchard Ave. Clovis, CA 93612</span></div>
</main>
</body>
</html>
```